Environmental Company Website
Kelvro Remediation website
Project: Environmental Company Website
Environmental Company Website - Environment
Creative Brief
Environment
www.kelvroremediation.example
We are an environmental cleanup/spill response company. We service Industrial and Municiple customers. Most of our work revolves around gas/petroleum spills or tank cleaning. We need to keep a very professional, emergency response image. We are not so different than a fire department in our emergency nature. We sell spill supplies to our customers, but we will not sell from our website.
Dislike busy, clumsy, long page websites. Looking for a one page length website (if possible). No scrolling needed to view the pages unless the content demands it. The home page fills the screen, but doesn't go down below the bottom of the window. The nav bar could be on the top or left, whatever best compliments the page.
Elegant
Black / Gray / White/ Blue (see logo)
Yellow
Your choice, we're open to ideas
Arial, Verdana
top
www.lorptank.example
http://www.mavulonsite.example/
http://www.wandertidebreaks.example/
Additional websites we like: http://www.hollisquay-horology.example/en2/ http://www.pinmoorcatch.example/ http://www.oakventhomefit.example/ http://tamworkbuilders.example/ http://www.quennabay.example/ourcatch/

```html
<!DOCTYPE html>
<html lang="en">
<head>
<meta charset="utf-8">
<title>Kelvro Remediation, LLC</title>
<link rel="stylesheet" href="https://fonts.googleapis.com/css2?family=Arimo:wght@400;700&family=Cinzel:wght@400;700&family=Tinos:wght@400;700&display=swap">
<style>
:root{
  --ink:#0c0c0c;
  --charcoal:#232323;
  --steel:#4a4a4a;
  --mist:#e9ebee;
  --paper:#ffffff;
  --blue:#2a5d9c;
  --blue-light:#6ea3d8;
  --orange:#d4500e;
  --gold:#b88a1c;
  --nav-text:#e4e4e4;
  --label-bar:rgba(20,20,20,.72);
}
*{box-sizing:border-box;margin:0;padding:0}
html,body{width:1200px;height:802px;overflow:hidden;background:var(--ink)}
body{font-family:"Arimo",Arial,sans-serif;position:relative}
.site{position:relative;width:1200px;height:802px;overflow:hidden;
  background:linear-gradient(180deg,#0a0a0a 0,#2c2c2c 140px,#3a3a3a 300px,#cfd3d8 460px,var(--mist) 520px,#f7f8f9 700px)}
.header-glow{position:absolute;left:0;top:0;width:1200px;height:460px;
  background:radial-gradient(ellipse 600px 200px at 600px 120px,rgba(120,120,120,.35),transparent 70%)}
.logo{position:absolute;left:26px;top:12px;width:264px;height:110px;background:linear-gradient(180deg,#fff,#dfe3e8);
  border:1px solid #9aa;box-shadow:0 3px 10px rgba(0,0,0,.6)}
.logo .mark{position:absolute;left:116px;top:12px;width:30px;height:30px;border-radius:50%;background:var(--blue)}
.logo-name{position:absolute;left:0;right:0;top:70px;text-align:center;white-space:nowrap;
  font-family:"Tinos","Times New Roman",serif;font-size:21px;line-height:24px;color:#1b2a3c;font-weight:400}
.phone{position:absolute;right:24px;top:14px;display:flex;align-items:center;gap:12px;color:var(--paper);font-size:19px;font-weight:700}
.phone svg{width:26px;height:26px}
.nav{position:absolute;left:427px;top:62px;width:756px;height:40px;display:flex;
  background:linear-gradient(180deg,#555,#1b1b1b);border:1px solid #777;border-radius:3px}
.nav a{flex:auto;display:flex;align-items:center;justify-content:center;color:var(--nav-text);text-decoration:none;
  font-size:12px;font-weight:700;border-right:1px solid #111;box-shadow:1px 0 0 #666}
.nav a:last-child{border-right:0;box-shadow:none}
.nav a.current{background:linear-gradient(180deg,#9a9a9a,#555);color:#f6c64b}
.banner{position:absolute;left:29px;top:140px;width:1140px;height:310px}
.panel{position:absolute;top:14px;height:282px;border:2px solid #cfd6de;box-shadow:0 0 12px rgba(0,0,0,.6)}
.panel .label{position:absolute;left:0;right:0;top:102px;height:28px;background:var(--label-bar);color:var(--paper);
  font-size:15px;font-weight:700;display:flex;align-items:center;justify-content:center}
.p-radiation{left:0;width:240px;background:linear-gradient(180deg,#7aa2c7,#3f5c7a 55%,#b08a18)}
.p-chemical{left:240px;width:210px;background:linear-gradient(180deg,#5d7fa6,#2f4a6a 60%,#9a4a1c)}
.p-gas{left:430px;top:0;width:300px;height:310px;z-index:2;border:3px solid var(--blue-light);
  box-shadow:0 0 22px rgba(110,163,216,.9);background:linear-gradient(180deg,#d7e6f4,#7e9ab5 50%,#39414a)}
.p-gas .label{top:118px}
.p-bio{left:715px;width:200px;background:linear-gradient(180deg,#6f8fa8,#55705a 55%,#2e3a2e)}
.p-industrial{left:915px;width:225px;background:linear-gradient(180deg,#b9c7d6,#7c8794 55%,#3d4650)}
.comments{position:absolute;left:32px;top:557px;width:228px;height:108px;border:1px solid #1d3e66;
  background:linear-gradient(180deg,#3f6d9e,#1f4572);padding:0 12px;color:var(--paper)}
.comments h3{font-size:10px;text-align:center;margin:3px 0 5px;color:#d8e6f4}
.field{display:flex;align-items:center;margin-bottom:4px;font-size:10px}
.field span{width:52px}
.field i{flex:1;height:12px;background:var(--paper);border:1px solid #8aa}
.msg{display:flex;font-size:10px}
.msg span{width:52px}
.msg i{flex:1;height:28px;background:var(--paper);border:1px solid #8aa}
.btn{display:inline-block;margin:4px 0 0 0;padding:2px 12px;background:linear-gradient(180deg,#e06a2a,#a83a08);
  color:var(--paper);font-size:10px;font-weight:700;border-radius:2px}
.welcome{position:absolute;left:292px;top:506px;width:880px}
.welcome .quote{position:absolute;left:0;top:22px;font-family:"Tinos",serif;font-size:66px;color:var(--blue);line-height:1}
.welcome h1{text-align:center;font-size:18px;font-weight:700;color:var(--orange);margin-bottom:14px}
.welcome h1 em{font-style:normal;color:var(--blue)}
.welcome p{text-indent:62px;font-size:12px;line-height:2.35;color:#222}
.read-more{display:inline-block;margin-left:8px;padding:2px 8px;background:var(--orange);color:var(--paper);font-size:9px;font-weight:700;vertical-align:middle;text-indent:0;line-height:1.4}
.tagline{position:absolute;left:290px;width:730px;top:664px;text-align:center;font-family:"Cinzel",serif;font-size:23px;color:var(--gold);font-weight:700;white-space:nowrap}
.footer{position:absolute;left:0;top:712px;width:1200px;height:90px;background:linear-gradient(180deg,#3a3a3a,#151515)}
.footer-links{position:absolute;left:0;width:1200px;top:30px;text-align:center;font-size:11px;font-weight:700;color:#f2a63a}
.copyright{position:absolute;left:29px;top:66px;font-size:9px;color:#cfcfcf}
.footer-name{position:absolute;right:28px;top:38px;font-family:"Tinos",serif;font-size:16px;color:var(--paper);white-space:nowrap}
</style>
</head>
<body>
<div class="site">
  <div class="header-glow"></div>
  <div class="logo"><span class="mark"></span><span class="logo-name">Kelvro Remediation, LLC</span></div>
  <div class="phone">
    <svg viewBox="0 0 24 24" aria-hidden="true"><path fill="#fff" d="M6.6 10.8c1.4 2.8 3.8 5.1 6.6 6.6l2.2-2.2c.3-.3.7-.4 1-.2 1.1.4 2.3.6 3.6.6.6 0 1 .4 1 1V20c0 .6-.4 1-1 1C10.6 21 3 13.4 3 4c0-.6.4-1 1-1h3.5c.6 0 1 .4 1 1 0 1.3.2 2.5.6 3.6.1.3 0 .7-.2 1z"/></svg>
    <span>CALL US 555-014-2290</span>
  </div>
  <nav class="nav">
    <a class="current" href="#">HOME</a><a href="#">ABOUT US</a><a href="#">SPILL RESPONSES</a><a href="#">EQUIPMENT</a><a href="#">CLEAN UP &amp; RESPONS</a><a href="#">SERVICES</a><a href="#">CONTACT</a>
  </nav>
  <section class="banner">
    <div class="panel p-radiation" role="img" aria-label="Yellow radiation waste barrels with hazard sign"><div class="label">Radiation Spill</div></div>
    <div class="panel p-chemical" role="img" aria-label="Offshore oil rig on the sea"><div class="label">Chemical Spill</div></div>
    <div class="panel p-bio" role="img" aria-label="White egrets standing in wetland water"><div class="label">Biological Spill</div></div>
    <div class="panel p-industrial" role="img" aria-label="Industrial refinery pipes and towers"><div class="label">Industrial</div></div>
    <div class="panel p-gas" role="img" aria-label="Collage of oil pump jacks and drilling derricks"><div class="label">Gas/Petroleum Spills</div></div>
  </section>
  <form class="comments">
    <h3>Give Your Comments!</h3>
    <div class="field"><span>Name</span><i></i></div>
    <div class="field"><span>E-Mail</span><i></i></div>
    <div class="msg"><span>Message</span><i></i></div>
    <span class="btn">SUBMIT</span>
  </form>
  <section class="welcome">
    <span class="quote">“</span>
    <h1>Welcome <em>To Our Site !</em></h1>
    <p>We are an environmental cleanup/spill response company. We service Industrial and Municiple customers. Most of our work revolves around gas/petroleum spills or tank cleaning. We need to keep a very professional, emergency response image. We are not so different than a fire department in our emergency nature. We sell spill supplies to our customers, but we will not sell from our website. <span class="read-more">READ MORE</span></p>
  </section>
  <div class="tagline">We Need to keep Clean in a very professional way...</div>
  <footer class="footer">
    <div class="footer-links">Home| About Us | Spill Respose | Equipment | Services | Clean Up &amp; Responses | Contact</div>
    <div class="copyright">© 2010 Corvane Web Studio, Inc All rights reserved</div>
    <div class="footer-name">Kelvro Remediation, LLC</div>
  </footer>
</div>
</body>
</html>
```